Business Card Design

our business is purchasing, rehabbing and flipping homes. Design a house in the palm of a hand. This card is for a new company based in Georgia. So we buy homes that have been foreclosed, short sales,abandond, old homes and vacant homes.
We help improve the communities that we work in. We would like to see designs that use a black background with green accent and other colors that blend and don't take away from the logo and other important information.

Industry/Entity Type

Business

Contact Information for Business Card

Hollow Pine Ventures
Turning Every Key Toward Home
2867 Ledgemoor Lane
Duluth GA 30096
Office: 678-555-0142
hollowpineventuresllc.example

```html
<!DOCTYPE html>
<html lang="en">
<head>
<meta charset="utf-8">
<title>Hollow Pine Ventures – Business Cards</title>
<link rel="stylesheet" href="https://fonts.googleapis.com/css2?family=Poppins:wght@300;500&display=swap">
<style>
  :root {
    --bg: #e9e9ea;
    --card: #111111;
    --ink: #ffffff;
    --accent: #2db673;
    --shadow: rgba(0, 0, 0, 0.28);
  }
  * { box-sizing: border-box; margin: 0; padding: 0; }
  html, body { width: 1200px; height: 800px; overflow: hidden; }
  body {
    background: var(--bg);
    font-family: "Poppins", sans-serif;
    font-weight: 300;
    color: var(--ink);
    display: flex;
    align-items: center;
    justify-content: center;
    gap: 60px;
  }
  .card {
    position: relative;
    width: 520px;
    height: 297px;
    background: var(--card);
    border-radius: 3px;
    box-shadow: 0 14px 30px var(--shadow);
    overflow: hidden;
  }
  .brand-mark {
    position: absolute;
    border-radius: 50%;
    background: var(--accent);
  }
  .brand-name {
    font-weight: 500;
    font-size: 22px;
    line-height: 1.1;
    letter-spacing: 0.2px;
    white-space: nowrap;
  }
  .tagline {
    font-size: 16px;
    line-height: 1.3;
    white-space: nowrap;
  }
  .contact { font-size: 14px; line-height: 1.75; }
  .contact-line { display: flex; align-items: center; gap: 8px; white-space: nowrap; }
  .contact-icon {
    width: 14px; height: 14px;
    display: inline-flex; align-items: center; justify-content: center;
    font-weight: 500; font-size: 15px;
    flex: none;
  }
  .contact-icon svg { width: 12px; height: 12px; fill: var(--ink); }

  /* Card one: mark left, name beside it */
  .card--side .brand-mark { width: 150px; height: 150px; left: 28px; top: 36px; }
  .card--side .brand-block { position: absolute; left: 196px; top: 62px; }
  .card--side .contact { position: absolute; left: 32px; bottom: 26px; }

  /* Card two: mark and name on the left half, contact on the right, address at the foot */
  .card--centre .brand-mark { width: 140px; height: 140px; left: 120px; top: 22px; }
  .card--centre .brand-block { position: absolute; left: 40px; width: 300px; top: 180px; text-align: center; }
  .card--centre .contact { position: absolute; right: 20px; top: 122px; font-size: 12.5px; line-height: 1.8; }
  .card--centre .address { position: absolute; left: 26px; bottom: 20px; font-size: 15px; white-space: nowrap; }
</style>
</head>
<body>

  <article class="card card--side">
    <span class="brand-mark" aria-hidden="true"></span>
    <div class="brand-block">
      <p class="brand-name">Hollow Pine Ventures</p>
      <p class="tagline">Turning Every Key Toward Home</p>
    </div>
    <div class="contact">
      <p class="contact-line">2867 Ledgemoor Lane Duluth GA 30096</p>
      <p class="contact-line">
        <span class="contact-icon"><svg viewBox="0 0 24 24" aria-hidden="true"><path d="M6.6 10.8a15.1 15.1 0 0 0 6.6 6.6l2.2-2.2a1 1 0 0 1 1-.25 11.4 11.4 0 0 0 3.6.57 1 1 0 0 1 1 1V20a1 1 0 0 1-1 1A17 17 0 0 1 3 4a1 1 0 0 1 1-1h3.5a1 1 0 0 1 1 1c0 1.25.2 2.45.57 3.57a1 1 0 0 1-.25 1z"/></svg></span>
        Office: 678-555-0142
      </p>
      <p class="contact-line"><span class="contact-icon">@</span>www.hollowpineventuresllc.example</p>
    </div>
  </article>

  <article class="card card--centre">
    <span class="brand-mark" aria-hidden="true"></span>
    <div class="contact">
      <p class="contact-line">
        <span class="contact-icon"><svg viewBox="0 0 24 24" aria-hidden="true"><path d="M6.6 10.8a15.1 15.1 0 0 0 6.6 6.6l2.2-2.2a1 1 0 0 1 1-.25 11.4 11.4 0 0 0 3.6.57 1 1 0 0 1 1 1V20a1 1 0 0 1-1 1A17 17 0 0 1 3 4a1 1 0 0 1 1-1h3.5a1 1 0 0 1 1 1c0 1.25.2 2.45.57 3.57a1 1 0 0 1-.25 1z"/></svg></span>
        Office: 678-555-0142
      </p>
      <p class="contact-line"><span class="contact-icon">@</span>www.hollowpineventuresllc.example</p>
    </div>
    <div class="brand-block">
      <p class="brand-name">Hollow Pine Ventures</p>
      <p class="tagline">Turning Every Key Toward Home</p>
    </div>
    <p class="address">2867 Ledgemoor Lane Duluth GA 30096</p>
  </article>

</body>
</html>
```